Pet Care company needs label design for new product. Eco-friendly, amazing results helping anima...

We need a label designed for a new eco-friendly pet care product. The product is highly effective, non-medicated, 100% safe to use on all animals. The product is an aqueous solution that uses a low PH to create an environment unfavorable for the grow of bacteria and fungus. Target market is horses, dogs and cats. Most common uses will be for rain rot, hot spots, ear infections and wound care. **Bottle is green with a white sprayer. Here is the specifications for the label; Trim size: 8.375 x 4.25 (w x h), please keep all critical art at least 1/8 inch away from trim line.Bleeds: Include 1/8 inch bleeds, and keep all critical art at least 1/8 inch away from trim line.

Target Market(s)

Pet owners; horses, dogs and cats

Industry/Entity Type

Pet Care

Font styles to use
Serif

Colors

Designer to choose colors to be used in the design.

Requirements
Must have
• Images of horses, dogs, cats. Geared to the eco-friendly nature of the product. It is not "organic" but I want that kind of look.
Nice to have
• Product information uploaded.
Should not have
• I do not want the product to look cartoonish. It is a highly effective treatment for animals with skin infections. I want people to feel by looking at the product it works.

```html
<!DOCTYPE html>
<html lang="en">
<head>
<meta charset="utf-8">
<title>Birch Balm – Eco-Friendly Pet Care Label</title>
<link href="https://fonts.googleapis.com/css2?family=Poppins:wght@300;400;600;700&display=swap" rel="stylesheet">
<style>
  :root {
    --page: #ffffff;
    --kraft: #c6ab80;
    --brand-green: #1d7a43;
    --band-green: #6f8b59;
    --panel-green: #7b9663;
    --text-light: #f3f1e8;
    --text-white: #ffffff;
  }
  * { margin: 0; padding: 0; box-sizing: border-box; }
  html, body {
    width: 1200px;
    height: 1000px;
    overflow: hidden;
    background: var(--page);
  }
  .canvas {
    position: relative;
    width: 1200px;
    height: 1000px;
    font-family: "Poppins", sans-serif;
  }
  .label {
    position: absolute;
    left: 435px;
    top: 316px;
    width: 316px;
    height: 544px;
    background: var(--kraft);
  }
  .brand-name {
    position: absolute;
    top: 168px;
    left: 0;
    width: 100%;
    text-align: center;
    font-size: 33px;
    font-weight: 600;
    color: var(--brand-green);
    letter-spacing: 0.5px;
    line-height: 1;
  }
  .tagline-band {
    position: absolute;
    top: 207px;
    left: 0;
    width: 100%;
    height: 30px;
    background: var(--band-green);
    color: var(--text-light);
    font-size: 20px;
    font-weight: 300;
    text-align: center;
    line-height: 30px;
  }
  .info-panel {
    position: absolute;
    top: 237px;
    left: 38px;
    width: 236px;
    bottom: 0;
    background: var(--panel-green);
    color: var(--text-white);
    text-align: center;
  }
  .uses {
    list-style: none;
    margin-top: 40px;
    font-size: 16.5px;
    font-weight: 600;
    line-height: 28.5px;
  }
  .description {
    position: absolute;
    top: 218px;
    left: 20px;
    right: 20px;
    font-size: 8.4px;
    font-weight: 400;
    line-height: 12.5px;
  }
  .volume {
    position: absolute;
    top: 285px;
    left: 0;
    width: 100%;
    font-size: 8px;
    font-weight: 700;
  }
</style>
</head>
<body>
  <div class="canvas">
    <section class="label">
      <h1 class="brand-name">BIRCH BALM</h1>
      <div class="tagline-band">Eco-Friendly Pet Care</div>
      <div class="info-panel">
        <ul class="uses">
          <li>Rain Rot</li>
          <li>Hot Spots</li>
          <li>Surface wounds</li>
          <li>Ringworm and More!</li>
        </ul>
        <p class="description">None medicated,safe,effective aid<br>providing a healing environment for<br>recovery from fungal and bacterial infections.</p>
        <p class="volume">16 fl oz - 473 ml</p>
      </div>
    </section>
  </div>
</body>
</html>
```